Eye catching Bottle label for pink gin targeting women 25+

We need a new label for a re-launch of our shimmering strawberry pink gin liqueur. We would like it to look premium and eye catching on the shelf. We have 2 labels we require, one for 200ml bottle (2x2 inches) and one for 500ml bottle 4x4 inches). Label must state the ml of the bottle abd that it is 18.75%Vol. Also say Shimmering Strawberry Gin Liqueur with the brand name at the top - Marlow Tide. We have a logo but it doesn't need to be used if it doesn't work with the design/colours. The gin is presented in a clear bottle and is pink and sparkly. See uploaded image for reference.

Target Market(s)

Women aged 25-45

Font styles to use
Decorative

Colors
f59296
fbd4d5
eea4c8

Requirements
Must have
• Bottle size - 500ml/200ml
• Must say 17.50% Vol
• Must have brand name - Marlow Tide
• Must have product name - Glistening Pink Raspberry
• Must say - Gin Liqueur
Nice to have
• Some sort of floral or swirley background detail would be nice
Should not have
• Must not appeal to children

```html
<!DOCTYPE html>
<html lang="en">
<head>
<meta charset="UTF-8">
<title>Marlow Tide – Glistening Pink Raspberry Labels</title>
<link href="https://fonts.googleapis.com/css2?family=Cinzel:wght@400;500;700&family=Arimo:wght@700&display=swap" rel="stylesheet">
<style>
  :root {
    --canvas: #ffffff;
    --size-tag: #e8232b;
    --brand-pink: #ec5f8c;
    --band-pink: #ef6590;
    --band-text: #ffffff;
    --detail-pink: #e2508a;
    --splash-coral: #f59296;
    --splash-blush: #fbd4d5;
    --splash-orchid: #eea4c8;
    --splash-rose: #f07fa6;
    --label-bg: #ffffff;
  }
  * { margin: 0; padding: 0; box-sizing: border-box; }
  html, body {
    width: 1200px;
    height: 804px;
    overflow: hidden;
    background: var(--canvas);
  }
  .board {
    position: relative;
    width: 1200px;
    height: 804px;
  }
  .size-tag {
    position: absolute;
    top: 38px;
    font-family: "Arimo", Arial, sans-serif;
    font-weight: 700;
    font-size: 19px;
    letter-spacing: 2px;
    color: var(--size-tag);
    transform: translateX(-50%);
    white-space: nowrap;
  }
  .size-tag--small { left: 274px; }
  .size-tag--large { left: 851px; }

  .label {
    position: absolute;
    background: var(--label-bg);
    box-shadow: 0 2px 10px rgba(0,0,0,0.22);
    overflow: hidden;
  }
  .label--small { left: 109px; top: 86px; width: 330px; height: 660px; }
  .label--large { left: 606px; top: 89px; width: 490px; height: 652px; }

  .brand {
    position: absolute;
    left: 0; right: 0;
    top: 28px;
    text-align: center;
    font-family: "Cinzel", "Times New Roman", serif;
    font-weight: 400;
    font-size: 30px;
    line-height: 1.1;
    letter-spacing: 1px;
    color: var(--brand-pink);
  }

  .splash {
    position: absolute;
    left: 0; right: 0;
    background:
      radial-gradient(ellipse at 30% 40%, var(--splash-rose) 0%, transparent 45%),
      radial-gradient(ellipse at 80% 55%, var(--splash-coral) 0%, transparent 50%),
      radial-gradient(ellipse at 50% 85%, var(--splash-blush) 0%, transparent 55%),
      linear-gradient(180deg, var(--label-bg) 0%, var(--splash-orchid) 30%, var(--splash-orchid) 75%, var(--splash-blush) 100%);
  }
  .label--small .splash { top: 128px; height: 348px; }
  .label--large .splash { top: 126px; height: 343px; }

  .name-band {
    position: absolute;
    left: 0; right: 0;
    background: var(--band-pink);
    display: flex;
    flex-direction: column;
    align-items: center;
    justify-content: center;
    text-align: center;
    font-family: "Cinzel", "Times New Roman", serif;
    font-weight: 400;
    text-transform: uppercase;
    color: var(--band-text);
    letter-spacing: 1px;
    white-space: nowrap;
  }
  .label--small .name-band { top: 476px; height: 148px; font-size: 36px; line-height: 42px; }
  .label--large .name-band { top: 469px; height: 146px; font-size: 47px; line-height: 45px; }

  .details {
    position: absolute;
    left: 0; right: 0;
    bottom: 0;
    display: flex;
    align-items: center;
    justify-content: center;
    font-family: "Cinzel", "Times New Roman", serif;
    font-weight: 500;
    color: var(--detail-pink);
    white-space: nowrap;
    letter-spacing: 0.5px;
  }
  .label--small .details { height: 36px; font-size: 17px; }
  .label--large .details { height: 37px; font-size: 18px; }
  .details .sep { margin: 0 7px; }
</style>
</head>
<body>
<main class="board">
  <p class="size-tag size-tag--small">2 x 4 inc</p>
  <p class="size-tag size-tag--large">3 x 4 inc</p>

  <section class="label label--small">
    <div class="brand">Marlow<br>Tide</div>
    <div class="splash" role="img" aria-label="Abstract watercolour splash artwork in pink, coral and blush tones"></div>
    <div class="name-band">
      <span>Glistening</span>
      <span>Pink</span>
      <span>Raspberry</span>
    </div>
    <div class="details">
      <span>Gin Liqueur</span><span class="sep">|</span><span>17.50% Vol</span><span class="sep">|</span><span>500 ML</span>
    </div>
  </section>

  <section class="label label--large">
    <div class="brand">Marlow<br>Tide</div>
    <div class="splash" role="img" aria-label="Abstract watercolour splash artwork in pink, coral and blush tones"></div>
    <div class="name-band">
      <span>Glistening</span>
      <span>Pink</span>
      <span>Raspberry</span>
    </div>
    <div class="details">
      <span>Gin Liqueur</span><span class="sep">|</span><span>17.50% Vol</span><span class="sep">|</span><span>500 ML</span>
    </div>
  </section>
</main>
</body>
</html>
```